Marketing Collateral Template Design

We are in the middle of rebranding and rolling out a new webiste. We would like to create collateral templates that match our new brand and style guide and are visually appealing to clients. The templates include:
- flyer one-pagers (data sheets)
- case studies
- whitepaper

We have the colors, font and basic design look/feel we want to use, we just need someone to leverage those elements and create templates that have a similar design but are unique as well (ie we want someone looking at a data sheet and a case study to know they are different materials, but from the same brand).

Primary Colors:
Darker BLUE (Red: 19 / Green: 67 / Blue: 113)
BLUE (Red: 15 / Green: 111 / Blue: 161)
Lighter BLUE (Red: 137 / Green: 153 / Blue: 228)

Font:
Headers: Gotham, Light
Body: Gotham, Book

Requirements
Must have
• Primary Colors:

Font:
Headers: Gotham, Light
Body: Gotham, Book
Should not have
• the templates should not have too much text

```html
<!DOCTYPE html>
<html lang="en">
<head>
<meta charset="utf-8">
<title>Veltrix – Optimize Your IT Infrastructure with Cloud</title>
<link rel="stylesheet" href="https://fonts.googleapis.com/css2?family=Montserrat:wght@300;400;500;600;700&display=swap">
<style>
  :root {
    --navy: #134371;
    --blue: #0f6fa1;
    --lavender: #8999e4;
    --lavender-pale: #e3e6f4;
    --ink: #222428;
    --muted: #8a8b99;
    --white: #ffffff;
  }
  * { box-sizing: border-box; margin: 0; padding: 0; }
  html, body { width: 927px; height: 1200px; overflow: hidden; background: var(--white); }
  body { font-family: "Montserrat", Arial, sans-serif; color: var(--ink); }
  .sheet { position: relative; width: 927px; height: 1200px; overflow: hidden; background: var(--white); }
  .abs { position: absolute; }

  .brand-bar { left: 0; top: 0; width: 368px; height: 85px; background: var(--navy); }
  .brand-name { left: 90px; top: 14px; font-size: 38px; font-weight: 700; color: var(--white); line-height: 1; letter-spacing: -0.5px; }
  .brand-tagline { left: 90px; top: 59px; font-size: 12.5px; font-weight: 400; color: var(--white); border-top: 1px solid var(--white); padding-top: 3px; }

  .hero-art { left: 0; top: 0; width: 927px; height: 600px; }

  .headline-box { left: 65px; top: 107px; width: 428px; height: 168px; background: var(--white); }
  .headline { left: 86px; top: 116px; font-size: 46px; font-weight: 300; line-height: 52px; color: var(--navy); white-space: nowrap; }
  .lede { left: 87px; top: 288px; font-size: 22.5px; font-weight: 300; line-height: 30px; color: var(--muted); white-space: nowrap; }

  .accent-tab { left: 0; top: 451px; width: 65px; height: 21px; background: var(--blue); }
  .section-title { font-size: 30px; font-weight: 300; color: var(--ink); line-height: 1; left: 87px; white-space: nowrap; }
  .body-copy { left: 87px; width: 476px; font-size: 14.5px; line-height: 20px; font-weight: 400; letter-spacing: -0.15px; color: var(--ink); text-align: justify; }
  .body-copy .ln { display: block; text-align-last: justify; white-space: nowrap; }
  .body-copy .ln.narrow { width: 380px; text-align-last: left; }
  .body-copy p + p { margin-top: 13px; }

  .services-bar { left: 648px; top: 580px; width: 279px; height: 21px; background: var(--blue); }
  .services-title { left: 650px; top: 623px; font-size: 18.5px; font-weight: 400; letter-spacing: 0.6px; color: var(--ink); white-space: nowrap; }
  .service { text-align: center; font-size: 14px; line-height: 18px; color: var(--ink); }
  .service svg { display: block; margin: 0 auto 6px; }

  .footer-rule { left: 0; top: 1050px; width: 562px; height: 6px; background: var(--navy); }
  .footer-brand { left: 87px; top: 1073px; font-size: 26px; font-weight: 700; color: var(--ink); line-height: 1; }
  .footer-tagline { left: 87px; top: 1101px; width: 145px; font-size: 7px; color: var(--ink); border-top: 1px solid var(--ink); padding-top: 2px; white-space: nowrap; }
  .partner-badge { left: 245px; top: 1078px; width: 78px; height: 32px; background: var(--navy); }
  .locations { left: 87px; top: 1124px; width: 236px; font-size: 12px; line-height: 15px; color: var(--ink); }
  .label { color: var(--blue); font-weight: 600; }
  .dot { color: var(--blue); }
  .hq { left: 352px; top: 1082px; font-size: 12px; line-height: 15.5px; color: var(--ink); }
  .hq .label { font-size: 12.5px; display: block; margin-bottom: 3px; }
  .hq .row { display: flex; gap: 5px; align-items: flex-start; }
  .hq .row svg { flex: none; margin-top: 2px; }

  .contact-panel { left: 605px; top: 968px; width: 322px; height: 232px; }
  .contact-text { left: 605px; top: 1022px; width: 322px; text-align: center; color: var(--white); }
  .contact-line { font-size: 21px; font-weight: 700; line-height: 29px; }
  .legal { margin-top: 6px; font-size: 11px; line-height: 13.5px; padding: 0 40px; }
</style>
</head>
<body>
<main class="sheet">
  <svg class="abs hero-art" viewBox="0 0 927 600" width="927" height="600">
    <defs>
      <linearGradient id="heroFill" x1="0" y1="0" x2="1" y2="1">
        <stop offset="0" stop-color="#0b4f7a"/>
        <stop offset="0.45" stop-color="#2a9fd6"/>
        <stop offset="0.8" stop-color="#10507e"/>
        <stop offset="1" stop-color="#1d2630"/>
      </linearGradient>
    </defs>
    <polygon points="362,0 927,0 927,458 735,586 362,404" fill="var(--lavender-pale)"/>
    <polygon points="390,0 927,0 927,434 735,566 390,394" fill="var(--lavender)"/>
    <polygon points="404,0 927,0 927,418 735,550 404,386" fill="url(#heroFill)" role="img" aria-label="Photo of a businessman touching a glowing cloud network interface"/>
  </svg>

  <div class="abs brand-bar"></div>
  <div class="abs brand-name">Veltrix</div>
  <div class="abs brand-tagline">Global Technology Solutions Provider</div>

  <div class="abs headline-box"></div>
  <h1 class="abs headline" style="font-weight:300">Optimize Your<br>IT Infrastructure<br>with Cloud</h1>
  <p class="abs lede">So condius, conum di<br>iamquideo iam quodi<br>us re permaximus co<br>ffrempe rcermius, nes</p>

  <div class="abs accent-tab"></div>
  <h2 class="abs section-title" style="top:452px;font-weight:300">Title Goes Here</h2>
  <div class="abs body-copy" style="top:499px">
    <p>
      <span class="ln narrow">Apernum pere remores ad merrae ermil</span>
      <span class="ln narrow">huidin hos, que cullerides in signove, nos, nici</span>
      <span class="ln">siliam til hum inius esidien imistilin vis sid senatque</span>
      <span class="ln">inte, contim omprae rem ime ad ips, sedem ad comne es</span>
      <span class="ln">ocri, sentrum, nique res ina, facrehe moervilicam si in dio</span>
      <span class="ln">eti, caetraelude fachus aus faceper ausperis; nes, uterude</span>
      <span class="ln" style="text-align-last:left">natifec emplius, tessid comniquit, tam publicatus.</span>
    </p>
  </div>

  <h2 class="abs section-title" style="top:675px;font-weight:300">Second Title Goes Here</h2>
  <div class="abs body-copy" style="top:722px">
    <p>
      <span class="ln">Apernum pere remores ad merrae ermil huidin hos, que</span>
      <span class="ln">culleride​s in signove, nos, nici siliam til hum inius esidien</span>
      <span class="ln">imistilin vis sid senatque inte, contim omprae rem ime</span>
      <span class="ln">ad ips, sedem ad comne es ocri, sentrum, nique res ina,</span>
      <span class="ln">facrehe moervilicam si in dio eti, caetraelude fachus aus</span>
      <span class="ln" style="text-align-last:left">faceper ausperis; nes, uterude natifec emplius,</span>
    </p>
    <p>
      <span class="ln">tessid comniquit,Irmil videtra vis. moverisse, utemovidena,</span>
      <span class="ln">ut gra? Quodiemod claribu nclessigna, nonsu vena, num</span>
      <span class="ln">poptiumTem int ceris habentius Mae verebem tam tem res</span>
      <span class="ln">videm patquam aute, tiam consuppli peri suler hoctum</span>
      <span class="ln">ceris hil condam, zori inte renit, serum tam publicatus</span>
      <span class="ln">cerum ubliisq Ga. Nam veniet eatet occabor ibuscip</span>
      <span class="ln">sandandisto ium qui dero im doloreperiae ped et doluptur</span>
      <span class="ln" style="text-align-last:left">minvers perspe con pro cus aborerumet vit ut voluptatur.</span>
    </p>
  </div>

  <div class="abs services-bar"></div>
  <h3 class="abs services-title" style="font-weight:400">ANOTHER TITLE HERE</h3>

  <div class="abs service" style="left:645px;top:674px;width:96px">
    <svg width="44" height="46" viewBox="0 0 44 46" fill="var(--blue)">
      <circle cx="22" cy="22" r="10"/><rect x="17" y="30" width="10" height="5"/><rect x="18" y="36" width="8" height="4" rx="1"/>
      <g stroke="var(--blue)" stroke-width="2.5" stroke-linecap="round"><line x1="22" y1="3" x2="22" y2="7"/><line x1="6" y1="10" x2="9" y2="13"/><line x1="38" y1="10" x2="35" y2="13"/><line x1="2" y1="23" x2="7" y2="23"/><line x1="42" y1="23" x2="37" y2="23"/></g>
    </svg>Discovery</div>

  <div class="abs service" style="left:800px;top:678px;width:80px">
    <svg width="44" height="42" viewBox="0 0 44 44" fill="none" stroke="var(--blue)" stroke-width="4">
      <path d="M22 6H8a3 3 0 0 0-3 3v27a3 3 0 0 0 3 3h27a3 3 0 0 0 3-3V22"/>
      <path d="M36 5l5 5-17 17h-5v-5z" fill="var(--blue)" stroke-width="2"/>
    </svg>Design</div>

  <div class="abs service" style="left:672px;top:764px;width:190px">
    <svg width="64" height="50" viewBox="0 0 64 50" fill="var(--blue)">
      <circle cx="22" cy="30" r="12"/>
      <g stroke="var(--blue)" stroke-width="5"><line x1="22" y1="14" x2="22" y2="46"/><line x1="6" y1="30" x2="38" y2="30"/><line x1="11" y1="19" x2="33" y2="41"/><line x1="33" y1="19" x2="11" y2="41"/></g>
      <circle cx="22" cy="30" r="4.5" fill="#fff"/>
      <circle cx="46" cy="13" r="8"/>
      <g stroke="var(--blue)" stroke-width="3.5"><line x1="46" y1="2" x2="46" y2="24"/><line x1="35" y1="13" x2="57" y2="13"/><line x1="38" y1="5" x2="54" y2="21"/><line x1="54" y1="5" x2="38" y2="21"/></g>
      <circle cx="46" cy="13" r="3" fill="#fff"/>
    </svg>Custom Development<br>&amp; Migration</div>

  <div class="abs service" style="left:645px;top:888px;width:100px">
    <svg width="46" height="46" viewBox="0 0 46 46" fill="none" stroke="var(--blue)" stroke-width="4.5">
      <path d="M20 6H7v33h33V26"/><path d="M19 27L39 7"/><path d="M26 5h15v15" fill="none"/>
    </svg>Deployment</div>

  <div class="abs service" style="left:800px;top:886px;width:80px">
    <svg width="48" height="48" viewBox="0 0 48 48" fill="none" stroke="var(--blue)">
      <circle cx="29" cy="18" r="12" stroke-width="5"/><line x1="20" y1="27" x2="6" y2="41" stroke-width="7" stroke-linecap="round"/>
    </svg>Testing</div>

  <div class="abs footer-rule"></div>
  <div class="abs footer-brand">Veltrix</div>
  <div class="abs footer-tagline">Global Technology Solutions Provider</div>
  <div class="abs partner-badge" role="img" aria-label="Partner badge"></div>
  <p class="abs locations"><span class="label">Locations:</span> Los Angeles <span class="dot">•</span> New York City <span class="dot">•</span> Orlando <span class="dot">•</span> Boston <span class="dot">•</span> Philadelphia <span class="dot">•</span> Washington DC <span class="dot">•</span> San Francisco <span class="dot">•</span> London <span class="dot">•</span> Hamburg <span class="dot">•</span> Hyderabad</p>

  <div class="abs hq">
    <span class="label">Corporate Headquarters:</span>
    <div class="row"><svg width="11" height="11" viewBox="0 0 12 12" fill="var(--blue)"><path d="M6 0l6 6h-2v6H7V8H5v4H2V6H0z"/></svg><span>1180 Harbor Crest, Suite<br>210, Riverton, CA 90210</span></div>
    <div class="row"><svg width="11" height="11" viewBox="0 0 12 12" fill="var(--blue)"><path d="M2 0l3 3-1.5 1.5a7 7 0 0 0 4 4L9 7l3 3-2 2C5 12 0 7 0 2z"/></svg><span>212.555.0178 or 800.555.0142</span></div>
    <div class="row"><svg width="11" height="11" viewBox="0 0 12 12" fill="var(--blue)"><rect x="3" y="0" width="6" height="4"/><rect x="0" y="4" width="12" height="5" rx="1"/><rect x="3" y="8" width="6" height="4"/></svg><span>212.555.0193</span></div>
    <div class="row"><svg width="11" height="11" viewBox="0 0 12 12" fill="none" stroke="var(--blue)" stroke-width="1.5"><rect x="1" y="2" width="10" height="8"/><path d="M1 2l5 4 5-4"/></svg><span>solutions@veltrix.com</span></div>
  </div>

  <svg class="abs contact-panel" viewBox="0 0 322 232" width="322" height="232">
    <polygon points="0,232 0,62 161,0 322,62 322,232" fill="var(--navy)"/>
  </svg>
  <div class="abs contact-text">
    <div class="contact-line">1-800-555-0142</div>
    <div class="contact-line">www.veltrix.com</div>
    <p class="legal">© 2013 Veltrix, Inc. All rights reserved. Veltrix is a registered servicemark of Veltrix, Inc. The Northgate logo and the Northgate Premier Business Partner mark are trademarks of Northgate Systems Corporation, registered in many jurisdictions worldwide.</p>
  </div>
</main>
</body>
</html>
```